Cleaning services Business Card Design

I need a business card design for my Cleaning business. I would like perhaps emphasis on the company name, Muddle to Marvel. Maybe the Muddle would to dirty and the marvel would have sprinkles.

Industry/Entity Type

Business

Contact Information for Business Card

Muddle to Marvel Cleaning Services, Teodoro Perlas, Industrial, Commercial, & Residential 418-635-0247

```html
<!DOCTYPE html>
<html lang="en">
<head>
<meta charset="utf-8">
<title>Muddle to Marvel Cleaning Services – Business Card</title>
<link href="https://fonts.googleapis.com/css2?family=Open+Sans:wght@400;700&display=swap" rel="stylesheet">
<style>
  :root {
    --backdrop: #e8ebee;
    --card: #ffffff;
    --teal: #1cb4c9;
    --navy: #17324a;
  }
  * { margin: 0; padding: 0; box-sizing: border-box; }
  html, body {
    width: 1200px;
    height: 1000px;
    overflow: hidden;
    background: var(--backdrop);
    font-family: "Open Sans", sans-serif;
  }
  .business-card {
    position: absolute;
    left: 60px;
    top: 178px;
    width: 1080px;
    height: 643px;
    background: var(--card);
    box-shadow: 0 4px 14px rgba(0, 0, 0, 0.18);
    color: var(--navy);
    text-align: center;
  }
  .brand {
    position: absolute;
    top: 100px;
    left: 0;
    right: 0;
    display: flex;
    justify-content: center;
    align-items: center;
    gap: 28px;
  }
  .brand-dot {
    width: 64px;
    height: 64px;
    border-radius: 50%;
    background: var(--teal);
    flex: none;
  }
  .brand-name {
    color: var(--teal);
    font-weight: 700;
    text-align: left;
    line-height: 1.1;
  }
  .brand-name .brand-main { display: block; font-size: 72px; }
  .brand-name .brand-sub { display: block; font-size: 34px; letter-spacing: 6px; }
  .contact-name {
    position: absolute;
    top: 408px;
    left: 0; right: 0;
    font-size: 45px;
    font-weight: 700;
    color: var(--teal);
  }
  .contact-phone {
    position: absolute;
    top: 474px;
    left: 0; right: 0;
    font-size: 31px;
    display: flex;
    justify-content: center;
    align-items: center;
    gap: 12px;
  }
  .contact-phone .label { font-weight: 700; }
  .contact-phone svg { width: 26px; height: 26px; fill: var(--navy); }
  .service-list {
    position: absolute;
    top: 560px;
    left: 0; right: 0;
    font-size: 29px;
    word-spacing: 4px;
  }
</style>
</head>
<body>
  <main class="business-card">
    <div class="brand">
      <span class="brand-dot"></span>
      <p class="brand-name">
        <span class="brand-main">Muddle to Marvel</span>
        <span class="brand-sub">Cleaning Services</span>
      </p>
    </div>

    <h1 class="contact-name">Teodoro Perlas</h1>

    <p class="contact-phone">
      <span class="label">Call us</span>
      <svg viewBox="0 0 24 24" aria-hidden="true">
        <path d="M6.6 10.8c1.4 2.8 3.8 5.1 6.6 6.6l2.2-2.2c.3-.3.7-.4 1-.2 1.1.4 2.3.6 3.6.6.6 0 1 .4 1 1V20c0 .6-.4 1-1 1C10.6 21 3 13.4 3 4c0-.6.4-1 1-1h3.5c.6 0 1 .4 1 1 0 1.3.2 2.5.6 3.6.1.3 0 .7-.2 1z"/>
      </svg>
      <span class="number">418-635-0247</span>
    </p>

    <p class="service-list">Industrial &nbsp;-&nbsp; Commercial &nbsp;-&nbsp; Residential</p>
  </main>
</body>
</html>
```